BLR Saddlebrooke Driveways

Looking for a post card for use in the KTRL Broad Lane Route Post program. Im looking to advertise my services as an installer of paver patios, driveways and walkways. Im willing to give a 10% discount for projects that exceed 2500 dollars. My qualifications include over 10 years exp, a masters degree in Landscape Architecture and I am licenced, insured and bonded. Company name is Corvel Terrafine LLC. Other services avail include irrigation services, planting services and landscape masonry. I am a builder of custom patios and landscapes. Im uploading my attempt at the mailer.

Reason: Have a few I like but they needed mods such as BLRP criteria included or pic modification.

```html
<!DOCTYPE html>
<html lang="en">
<head>
<meta charset="utf-8">
<title>Corvel Terrafine LLC – Postcard</title>
<link href="https://fonts.googleapis.com/css2?family=Bebas+Neue&family=Open+Sans:wght@400;600&family=Libre+Baskerville:ital@1&display=swap" rel="stylesheet">
<style>
  :root {
    --stage: #2b2b2b;
    --leaf-green: #a2c43a;
    --clay-orange: #d3622e;
    --sun-yellow: #f6ec2f;
    --sand-text: #f7d98a;
    --white: #ffffff;
    --card-back: #f4f4f4;
    --ink: #1c1c1c;
    --grey-brand: #a7a7a7;
    --rule: #333333;
  }
  * { margin: 0; padding: 0; box-sizing: border-box; }
  html, body { width: 800px; height: 1200px; overflow: hidden; }
  body { background: var(--stage); position: relative; font-family: "Open Sans", Arial, sans-serif; }

  .card { position: absolute; left: 94px; width: 614px; height: 453px; box-shadow: 0 4px 14px rgba(0,0,0,.55); }
  .card-front { top: 119px; }
  .card-back { top: 632px; background: radial-gradient(ellipse at 55% 45%, #ffffff 0%, var(--card-back) 60%, #e6e6e6 100%); }

  .brand-panel { position: absolute; left: 0; top: 0; width: 209px; height: 199px; background: var(--leaf-green); }
  .brand-mark { position: absolute; left: 86px; top: 30px; width: 38px; height: 38px; border-radius: 50%; background: var(--white); }
  .brand-name { position: absolute; left: 0; width: 100%; text-align: center; font-family: "Bebas Neue", Impact, sans-serif; line-height: 1; }
  .brand-name-main { top: 106px; font-size: 64px; color: var(--sun-yellow); }
  .brand-name-sub { top: 165px; font-size: 29px; color: var(--white); }

  .offer-panel { position: absolute; left: 0; top: 199px; width: 209px; height: 254px; background: var(--clay-orange); font-family: "Bebas Neue", Impact, sans-serif; line-height: 1; }
  .offer-rate { position: absolute; left: 26px; top: 8px; font-size: 138px; color: var(--white); }
  .offer-rate sup { font-size: 70px; vertical-align: top; position: relative; top: 6px; }
  .offer-label { position: absolute; left: 28px; top: 128px; font-size: 55px; color: var(--white); }
  .offer-terms { position: absolute; left: 29px; font-size: 25px; color: var(--sand-text); }
  .offer-terms-1 { top: 180px; }
  .offer-terms-2 { top: 213px; }

  .hero-photo { position: absolute; left: 209px; top: 0; width: 405px; height: 453px;
    background: linear-gradient(180deg, #a9b3b9 0%, #7d8a5a 18%, #8a7a5e 34%, #a08a84 55%, #8e7670 78%, #7a625c 100%); }
  .service-tags { position: absolute; left: 464px; top: 20px; color: var(--white); line-height: 1.05; }
  .service-tags-lead { font-size: 36px; font-weight: 600; }
  .service-tags-item { font-size: 14px; }
  .service-tags-item.small { font-size: 11px; font-weight: 600; }
  .experience-note { position: absolute; right: 28px; bottom: 22px; color: var(--white); font-family: "Libre Baskerville", Georgia, serif; font-style: italic; line-height: 1; }
  .experience-note .lead { font-size: 15px; }
  .experience-note .big { font-size: 36px; }
  .experience-note .tail { position: absolute; right: 0; top: 36px; font-size: 13px; }

  .contact-block { position: absolute; left: 43px; top: 40px; font-size: 12px; line-height: 1.35; color: var(--ink); }
  .contact-block p + p { margin-top: 16px; }
  .services-block { position: absolute; left: 43px; top: 158px; width: 290px; color: var(--ink); }
  .services-title { font-size: 13px; font-weight: 600; margin-bottom: 10px; }
  .services-copy { font-size: 8px; line-height: 1.4; margin-bottom: 10px; }
  .services-list { list-style: none; font-size: 8px; line-height: 1.9; margin-top: 14px; }

  .divider { position: absolute; left: 404px; top: 36px; width: 1px; height: 384px; background: var(--rule); }
  .back-brand { position: absolute; left: 404px; right: 0; text-align: center; font-family: "Bebas Neue", Impact, sans-serif; color: var(--grey-brand); line-height: 1; }
  .back-brand-main { top: 34px; font-size: 64px; }
  .back-brand-sub { top: 95px; font-size: 29px; }
  .back-web { position: absolute; left: 404px; right: 0; top: 160px; text-align: center; font-size: 10px; color: var(--grey-brand); }
  .address-line { position: absolute; left: 442px; width: 135px; height: 1px; background: var(--rule); }
</style>
</head>
<body>
  <section class="card card-front">
    <div class="brand-panel">
      <span class="brand-mark"></span>
      <div class="brand-name brand-name-main">Corvel</div>
      <div class="brand-name brand-name-sub">Terrafine LLC</div>
    </div>
    <div class="offer-panel">
      <div class="offer-rate">10<sup>%</sup></div>
      <div class="offer-label">Discount</div>
      <div class="offer-terms offer-terms-1">For projects that</div>
      <div class="offer-terms offer-terms-2">exceed 2500 $</div>
    </div>
    <div class="hero-photo" role="img" aria-label="Photo of a desert backyard with cacti, gravel, boulders, flagstone path and a pool, mountains behind"></div>
    <div class="service-tags">
      <div class="service-tags-lead">Design</div>
      <div class="service-tags-item">Installations</div>
      <div class="service-tags-item small">Patios, Driveways, Walkways</div>
    </div>
    <div class="experience-note">
      <span class="lead">over </span><span class="big">10 years</span>
      <span class="tail">experience</span>
    </div>
  </section>

  <section class="card card-back">
    <div class="contact-block">
      <p>Terrafine Inc.<br>1418 E Marlow St<br>Tucson, AZ 85719</p>
      <p>Phone: 520-555-0147<br>Email: office@corvelterrafine.com</p>
    </div>
    <div class="services-block">
      <h2 class="services-title">SERVICES</h2>
      <p class="services-copy">Corvel Terrafine Inc is a licensed, insured and bonded landscape company specializing in paver patios, driveways and walkways.</p>
      <p class="services-copy">As the owner of Terrafine I hold a BS in Horticulture and a Masters of landscape Architecture. I have spent over 10 years in the field designing, building and maintaining landscapes. I am confident in my areas of specialization, however I and my team have extensive experience with many aspects of landscaping.</p>
      <ul class="services-list">
        <li>Paver Patios</li>
        <li>Driveways and Walkways</li>
        <li>Water Features</li>
        <li>Landscape Lighting</li>
        <li>Ramada Construction</li>
        <li>Irrigation Services</li>
        <li>Planting Services</li>
        <li>Landscape Masonry</li>
        <li>Grading and Drainage</li>
      </ul>
    </div>
    <div class="divider"></div>
    <div class="back-brand back-brand-main">Corvel</div>
    <div class="back-brand back-brand-sub">Terrafine LLC</div>
    <div class="back-web">www.corvelterrafine.com</div>
    <div class="address-line" style="top:331px"></div>
    <div class="address-line" style="top:358px"></div>
    <div class="address-line" style="top:385px"></div>
    <div class="address-line" style="top:412px"></div>
  </section>
</body>
</html>
```